High-end personal training needs a business card and logo

We need a modern business card design for a new personal training business based in the Jersey City and New York City area called 'Torvexa Training' .

We would like designs with a sky blue (hex #007ECC is a good start for the primary color) and dark black or slate background. We otherwise don't have a font or anything else. The final design should leave space for:
* A photo
* QR code
* Specialties & certifications
* Phone number
* Website
* Email

We have a rough idea of the logo but might need cleaning up and modernizing.

Here are some good starts of design styles and theme:
https://www.plumaworks.com/design/7261935
https://www.plumaworks.com/design/26370718
https://www.plumaworks.com/design/41827563

Contact Information for Business Card

Phone, email, QR code, website, specialties & certifications, room for photo, name

Colors

Designer to choose colors to be used in the design.

Requirements
Nice to have
• Experimentation on a logo that appeals to women but not too feminine (since we specialize in weightlifting, nutrition)

```html
<!DOCTYPE html>
<html lang="en">
<head>
<meta charset="utf-8">
<title>Torvexa Training — Business Card</title>
<link rel="stylesheet" href="https://fonts.googleapis.com/css2?family=Arimo:wght@400;700&display=swap">
<style>
  :root {
    --brand-blue: #007ECC;
    --ink: #2b2b2b;
    --paper: #ffffff;
    --backdrop: #e9ebee;
  }
  * { box-sizing: border-box; margin: 0; padding: 0; }
  html, body { width: 1200px; height: 892px; overflow: hidden; }
  body {
    background: var(--backdrop);
    font-family: "Arimo", Arial, sans-serif;
    position: relative;
  }
  .card {
    position: absolute;
    width: 560px;
    height: 320px;
    left: 320px;
    overflow: hidden;
    box-shadow: 0 6px 18px rgba(0,0,0,0.18);
  }
  .card-front { top: 90px; background: var(--paper); }
  .card-back { top: 470px; background: var(--brand-blue); }
  .card-art { position: absolute; inset: 0; width: 100%; height: 100%; }

  /* front */
  .brand-block {
    position: absolute;
    left: 34px; top: 92px;
    width: 210px;
    display: flex; align-items: center; gap: 10px;
  }
  .brand-dot {
    width: 18px; height: 18px; border-radius: 50%;
    background: var(--brand-blue); flex: none;
  }
  .brand-name {
    color: var(--brand-blue);
    font-weight: 700;
    font-size: 30px;
    line-height: 1.05;
    letter-spacing: 0.5px;
  }
  .divider {
    position: absolute;
    left: 262px; top: 62px;
    width: 2px; height: 140px;
    background: var(--brand-blue);
  }
  .contact-block {
    position: absolute;
    left: 288px; top: 64px;
    color: var(--ink);
  }
  .person-name { font-size: 15px; letter-spacing: 0.6px; }
  .person-title { font-size: 14px; letter-spacing: 0.6px; margin: 2px 0 14px 14px; }
  .contact-list { list-style: none; }
  .contact-item {
    display: flex; align-items: center; gap: 10px;
    font-size: 9px; letter-spacing: 0.4px;
    margin-bottom: 8px;
  }
  .contact-icon { width: 11px; height: 11px; fill: var(--brand-blue); flex: none; }

  /* back */
  .back-brand {
    position: absolute;
    left: 0; right: 0; top: 118px;
    display: flex; justify-content: center; align-items: center; gap: 14px;
  }
  .back-brand .brand-dot { background: var(--paper); width: 22px; height: 22px; }
  .back-brand .brand-name { color: var(--paper); font-size: 40px; }
  .back-website {
    position: absolute; left: 0; right: 0; top: 186px;
    text-align: center;
    color: var(--paper);
    font-size: 12px; letter-spacing: 1px;
  }
</style>
</head>
<body>

<section class="card card-front" aria-label="Business card front">
  <svg class="card-art" viewBox="0 0 560 320" aria-hidden="true">
    <path d="M150 320 C330 318 480 290 560 222 L560 320 Z" fill="var(--brand-blue)"/>
    <path d="M170 294 C330 298 470 272 530 226" fill="none" stroke="var(--brand-blue)" stroke-width="3" stroke-linecap="round"/>
  </svg>

  <div class="brand-block">
    <span class="brand-dot"></span>
    <span class="brand-name">Torvexa Training</span>
  </div>

  <div class="divider"></div>

  <div class="contact-block">
    <p class="person-name">YOUR NAME LASTNAME</p>
    <p class="person-title">MANAGING DIRECTOR</p>
    <ul class="contact-list">
      <li class="contact-item">
        <svg class="contact-icon" viewBox="0 0 24 24"><path d="M12 2a7 7 0 0 0-7 7c0 5 7 13 7 13s7-8 7-13a7 7 0 0 0-7-7zm0 9.5A2.5 2.5 0 1 1 12 6.5a2.5 2.5 0 0 1 0 5z"/></svg>
        YOUR LOCATION HERE
      </li>
      <li class="contact-item">
        <svg class="contact-icon" viewBox="0 0 24 24"><path d="M2 5h20v14H2z M2 5l10 8 10-8" fill="var(--brand-blue)"/><path d="M3 6l9 7 9-7" fill="none" stroke="#fff" stroke-width="1.6"/></svg>
        YOUR EMAIL DETAIL
      </li>
      <li class="contact-item">
        <svg class="contact-icon" viewBox="0 0 24 24"><circle cx="12" cy="12" r="10"/><path d="M2 12h20M12 2c3 3 3 17 0 20M12 2c-3 3-3 17 0 20" fill="none" stroke="#fff" stroke-width="1.4"/></svg>
        WWW.YOURWEBSITE.COM
      </li>
      <li class="contact-item">
        <svg class="contact-icon" viewBox="0 0 24 24"><path d="M6.6 10.8a15 15 0 0 0 6.6 6.6l2.2-2.2a1 1 0 0 1 1-.25 11.4 11.4 0 0 0 3.6.57 1 1 0 0 1 1 1V20a1 1 0 0 1-1 1A17 17 0 0 1 3 4a1 1 0 0 1 1-1h3.5a1 1 0 0 1 1 1c0 1.25.2 2.45.57 3.57a1 1 0 0 1-.25 1z"/></svg>
        01 8000 00 00
      </li>
    </ul>
  </div>
</section>

<section class="card card-back" aria-label="Business card back">
  <svg class="card-art" viewBox="0 0 560 320" aria-hidden="true">
    <path d="M0 0 L250 0 C150 8 60 40 0 92 Z" fill="var(--paper)"/>
    <path d="M30 90 C100 50 170 28 240 22" fill="none" stroke="var(--paper)" stroke-width="3" stroke-linecap="round"/>
    <path d="M560 232 C480 290 400 314 300 320 L560 320 Z" fill="var(--paper)"/>
    <path d="M300 300 C390 298 470 272 530 236" fill="none" stroke="var(--paper)" stroke-width="3" stroke-linecap="round"/>
  </svg>

  <div class="back-brand">
    <span class="brand-dot"></span>
    <span class="brand-name">Torvexa Training</span>
  </div>
  <p class="back-website">WWW.YOUREBSITE.COM</p>
</section>

</body>
</html>
```